I need a business card design for my new clinic (ATHLETIC CARE OF JOINT). I am orthopedist, expert in sports surgery, especially knee surgery. I prefer, as colors, the colors of my logo (green, black and white). I already have my logo and should appear on my card. It's good to see my site to have ideas (www.drlucianovarela.example)
It needs contain:
my name: Dr. Luciano Varela
my registration: CRM 584-902
my specialty: Cirurgia do Joelho / Esporte
my address: Centro Empresarial - Parque Aurora Mall
Av. Doutor Augusto Valadares Pinto, 2740 sala 803
Jd. Acácias - Ribeirão Preto - SP
my phone number: Tel (16) 8420-5937
my clinic phone: (16) 3745-8081
my e-mail: drlucianovarela@mailbox.example
my site: www.drlucianovarela.example

Target Market(s)

futures patients

Industry/Entity Type

Clinic

Requirements
Nice to have
• letters not overfilled
straight lines, with few curves

```html
<!DOCTYPE html>
<html lang="pt">
<head>
<meta charset="utf-8">
<title>Dr. Luciano Varela – Business Card</title>
<link rel="stylesheet" href="https://fonts.googleapis.com/css2?family=Tinos:wght@400;700&display=swap">
<style>
  :root {
    --stage: #2a2a2a;
    --card-black: #050505;
    --card-white: #ffffff;
    --brand-green: #3dbb7c;
    --text-light: #f2f2f2;
    --ink: #111111;
  }
  html, body {
    margin: 0;
    padding: 0;
    width: 1200px;
    height: 900px;
    overflow: hidden;
    background: var(--stage);
    font-family: "Tinos", "Times New Roman", serif;
  }
  .canvas {
    position: relative;
    width: 1200px;
    height: 900px;
  }
  .card {
    position: absolute;
    top: 300px;
    width: 520px;
    height: 300px;
    border-radius: 30px;
    overflow: hidden;
    background: var(--card-black);
  }
  .card--back { left: 60px; }
  .card--front { left: 620px; }

  /* Back side */
  .back-mark {
    position: absolute;
    inset: 0;
    display: flex;
    align-items: center;
    justify-content: center;
    gap: 18px;
  }
  .back-mark__square {
    width: 46px;
    height: 46px;
    background: var(--brand-green);
  }
  .back-mark__name {
    color: var(--text-light);
    font-size: 52px;
    font-weight: 700;
    letter-spacing: 1px;
  }

  /* Front side */
  .front-shapes {
    position: absolute;
    inset: 0;
  }
  .brand {
    position: absolute;
    left: 42px;
    top: 38px;
    display: flex;
    align-items: center;
    gap: 14px;
  }
  .brand__square {
    width: 40px;
    height: 40px;
    background: var(--brand-green);
  }
  .brand__name {
    color: var(--ink);
    font-size: 48px;
    font-weight: 700;
    line-height: 1;
    letter-spacing: 1px;
  }
  .doctor {
    position: absolute;
    left: 44px;
    top: 162px;
  }
  .doctor__name {
    margin: 0;
    color: var(--brand-green);
    font-size: 21px;
    font-weight: 400;
    line-height: 1.1;
  }
  .doctor__specialty {
    margin: 2px 0 0;
    color: var(--text-light);
    font-size: 11.5px;
  }
  .address {
    position: absolute;
    left: 44px;
    top: 214px;
    margin: 0;
    font-style: normal;
    color: var(--text-light);
    font-size: 11.5px;
    line-height: 1.35;
  }
  .contacts {
    position: absolute;
    left: 318px;
    top: 200px;
    margin: 0;
    padding: 0;
    list-style: none;
    color: var(--text-light);
    font-size: 11.5px;
    line-height: 1.35;
  }
  .contacts__label { color: var(--brand-green); }
  .contacts__gap { margin-top: 12px; }
</style>
</head>
<body>
<main class="canvas">

  <section class="card card--back" aria-label="Card back">
    <div class="back-mark">
      <span class="back-mark__square"></span>
      <span class="back-mark__name">VARELA</span>
    </div>
  </section>

  <section class="card card--front" aria-label="Card front">
    <svg class="front-shapes" width="520" height="300" viewBox="0 0 520 300" aria-hidden="true">
      <path d="M0,0 H520 V196 C400,190 220,148 0,120 Z" fill="var(--card-white)"/>
      <path d="M0,104 C150,118 300,160 430,194 C300,172 150,136 0,122 Z" fill="var(--brand-green)"/>
      <path d="M58,124 L96,131 L76,150 Z" fill="var(--card-white)" stroke="var(--brand-green)" stroke-width="1.5"/>
    </svg>

    <div class="brand">
      <span class="brand__square"></span>
      <span class="brand__name">VARELA</span>
    </div>

    <div class="doctor">
      <h1 class="doctor__name">Dr. Luciano Varela</h1>
      <p class="doctor__specialty">Cirurgia do Joelho / Esporte</p>
    </div>

    <address class="address">
      Centro Empresarial - Parque Aurora Mall<br>
      Av. Doutor Augusto Valadares Pinto, 2740 sala 803<br>
      Jd. Acácias - Ribeirão Preto - SP
    </address>

    <ul class="contacts">
      <li><span class="contacts__label">registration:</span> CRM 584-902</li>
      <li><span class="contacts__label">phone number:</span> (16) 8420-5937</li>
      <li class="contacts__gap"><span class="contacts__label">clinic phone:</span> (16) 3745-8081</li>
      <li><span class="contacts__label">email:</span> drlucianovarela@mailbox.example</li>
      <li><span class="contacts__label">website:</span> www.drlucianovarela.example</li>
    </ul>
  </section>

</main>
</body>
</html>
```